Business Card for By Karel Voss

Looking to have a business card designed for my lifestyle and fitness company. My company offers personal training, online programming and nutrition advice based out of London, United Kingdom.

I'd like to see modern, sleek designs, focusing on black, matte black or matte grey. Design doesn't need to be overly descriptive as this will also be used as a personal business card. I've included my logo.

Please note that my company is no longer called "Fitness by Karel Voss" but instead "By Karel Voss", this is because of my other ventures. Therefore please don't use the "fitness by karel voss" text.

information about my company can be found at www.bykarelvoss.com

Company is also based out of London (United Kingdom) & Sydney (Australia) this could be reflected on the card.

Industry/Entity Type

Business

Contact Information for Business Card

Karel Voss
+44 7382 615027
karel@bykarelvoss.com
www.bykarelvoss.com

Font styles to use
Sans Serif

Requirements
Must have
• All contact details and inclusion of my logo.

```html
<!DOCTYPE html>
<html lang="en">
<head>
<meta charset="utf-8">
<title>By Karel Voss — Business Card</title>
<link rel="stylesheet" href="https://fonts.googleapis.com/css2?family=Russo+One&family=Open+Sans:wght@400;600&display=swap">
<style>
  :root {
    --page: #e6e6e4;
    --card-white: #ffffff;
    --card-black: #231f20;
    --stripe-grey: #4a4748;
    --text-dark: #231f20;
    --text-light: #ffffff;
    --text-muted: #bdbbbb;
  }
  * { box-sizing: border-box; margin: 0; padding: 0; }
  html, body { width: 1200px; height: 800px; overflow: hidden; }
  body {
    background: var(--page);
    font-family: "Open Sans", Arial, sans-serif;
  }
  .canvas {
    position: relative;
    width: 1200px;
    height: 800px;
    display: flex;
    align-items: center;
    justify-content: center;
    gap: 50px;
  }
  .card {
    position: relative;
    width: 525px;
    height: 300px;
    overflow: hidden;
    box-shadow: 0 6px 18px rgba(0,0,0,0.18);
  }
  .card--front { background: var(--card-white); }
  .card--back { background: var(--card-black); }

  .card__shape { position: absolute; inset: 0; width: 100%; height: 100%; }

  .brand {
    position: absolute;
    display: flex;
    align-items: center;
    gap: 10px;
    font-family: "Russo One", Arial, sans-serif;
    text-transform: uppercase;
    letter-spacing: 0.5px;
    line-height: 1;
    white-space: nowrap;
  }
  .brand__dot {
    width: 32px;
    height: 32px;
    border-radius: 50%;
    flex: none;
  }
  .brand__name { font-size: 24px; }

  .card--front .brand { left: 34px; top: 100px; color: var(--text-dark); }
  .card--front .brand__dot { background: var(--text-dark); }

  .card--back .brand {
    left: 50%; top: 50%;
    transform: translate(-50%, -50%);
    color: var(--text-light);
  }
  .card--back .brand__dot { background: var(--text-light); }

  .contact {
    position: absolute;
    left: 34px;
    bottom: 22px;
    color: var(--text-light);
  }
  .contact__name { font-size: 16px; font-weight: 400; line-height: 21px; }
  .contact__role { font-size: 9px; line-height: 12px; color: var(--text-muted); margin-bottom: 8px; }
  .contact__list { list-style: none; }
  .contact__item {
    display: flex;
    align-items: center;
    gap: 8px;
    font-size: 11px;
    line-height: 17px;
  }
  .contact__icon { width: 11px; height: 11px; fill: none; stroke: var(--text-light); stroke-width: 1.4; flex: none; }
</style>
</head>
<body>
<main class="canvas">

  <section class="card card--front" aria-label="Business card front">
    <svg class="card__shape" viewBox="0 0 525 300" aria-hidden="true">
      <path d="M0,178 L255,178 C300,178 300,142 345,142 L525,142 L525,300 L0,300 Z" fill="var(--card-black)"/>
      <path d="M245,166 C288,166 292,128 338,128 L525,128" fill="none" stroke="var(--stripe-grey)" stroke-width="7"/>
    </svg>

    <div class="brand">
      <span class="brand__dot"></span>
      <span class="brand__name">By Karel Voss</span>
    </div>

    <div class="contact">
      <p class="contact__name">Karel Voss</p>
      <p class="contact__role">Director</p>
      <ul class="contact__list">
        <li class="contact__item">
          <svg class="contact__icon" viewBox="0 0 12 12"><path d="M2.5 1.5l2 2-1 1.2c.6 1.4 1.5 2.3 2.8 2.8l1.2-1 2 2-1.2 1.5C5.5 9.8 2.2 6.5 1 2.7z"/></svg>
          <span>+44 7382 615027</span>
        </li>
        <li class="contact__item">
          <svg class="contact__icon" viewBox="0 0 12 12"><rect x="1" y="2.5" width="10" height="7"/><path d="M1 2.5l5 4 5-4"/></svg>
          <span>karel@bykarelvoss.com</span>
        </li>
        <li class="contact__item">
          <svg class="contact__icon" viewBox="0 0 12 12"><circle cx="6" cy="6" r="5"/><path d="M1 6h10M6 1c-2.5 3-2.5 7 0 10M6 1c2.5 3 2.5 7 0 10"/></svg>
          <span>www.bykarelvoss.com</span>
        </li>
      </ul>
    </div>
  </section>

  <section class="card card--back" aria-label="Business card back">
    <div class="brand">
      <span class="brand__dot"></span>
      <span class="brand__name">By Karel Voss</span>
    </div>
  </section>

</main>
</body>
</html>
```